EDDM Mailer for Copper Kettle Repair

We need an EDDM sized postcard for our auto repair business promoting that we now offer free pick up and delivery of vehicles in the Solanco area as well as free loaner vehicles. Our logo, and a copy of our current post card are attached for reference. Please promote the business in general and highlight the pick up drop off loaner service that is new.

```html
<!DOCTYPE html>
<html lang="en">
<head>
<meta charset="utf-8">
<title>Copper Kettle Repair – EDDM Mailer</title>
<link rel="stylesheet" href="https://fonts.googleapis.com/css2?family=Poppins:wght@400;500;600&family=Russo+One&family=Mrs+Saint+Delafield&display=swap">
<style>
  :root {
    --backdrop: #8eaad4;
    --paper: #ffffff;
    --ink: #111111;
    --text: #222222;
    --green: #8bb84a;
    --blue: #5ec8f2;
    --blue-light: #a9dcf7;
  }
  * { margin: 0; padding: 0; box-sizing: border-box; }
  html, body { width: 875px; height: 1200px; overflow: hidden; }
  body { background: var(--backdrop); position: relative; font-family: "Poppins", sans-serif; color: var(--text); }

  .postcard { position: absolute; left: 98px; width: 680px; height: 500px; background: var(--paper); overflow: hidden; box-shadow: 0 8px 14px rgba(0,0,0,.18); }
  .postcard--front { top: 88px; }
  .postcard--back { top: 612px; }

  .abs { position: absolute; }
  .photo-frame, .photo { position: absolute; left: 0; top: 0; }

  /* front */
  .brand { left: 38px; top: 62px; display: flex; align-items: center; gap: 6px; font-weight: 600; font-size: 15px; color: var(--ink); }
  .brand__dot { width: 14px; height: 14px; border-radius: 50%; background: var(--ink); }
  .pickup-banner { left: 394px; top: 53px; width: 286px; height: 55px; background: var(--green); clip-path: polygon(14px 0, 100% 0, 100% 100%, 0 100%); border-radius: 6px 0 0 6px; padding: 5px 0 0 40px; font-size: 18px; line-height: 22px; color: #222; }
  .script { font-family: "Mrs Saint Delafield", cursive; }
  .tagline-script { left: 150px; top: 118px; font-size: 44px; color: var(--ink); }
  .headline { font-family: "Russo One", sans-serif; color: var(--ink); line-height: 1; white-space: nowrap; }
  .headline--auto { left: 36px; top: 158px; font-size: 88px; letter-spacing: 2px; }
  .headline--repair { left: 38px; top: 228px; font-size: 96px; letter-spacing: -1px; }
  .amp { left: 40px; top: 282px; font-size: 110px; color: var(--green); }
  .subhead { left: 128px; top: 318px; font-size: 32px; font-weight: 500; line-height: 32px; color: var(--ink); }
  .info-band { left: 0; top: 416px; width: 340px; height: 54px; background: var(--blue); padding: 10px 0 0 38px; font-size: 11.5px; line-height: 18px; color: #1a1a1a; }
  .info-band p { display: flex; align-items: center; gap: 8px; }
  .call-box { left: 304px; top: 405px; width: 191px; height: 78px; background: var(--green); border-radius: 12px; transform: skewX(-18deg); }
  .call-text { left: 314px; top: 415px; width: 180px; text-align: center; font-family: "Russo One", sans-serif; font-style: italic; transform: skewX(-10deg); }
  .call-text__label { font-size: 19px; color: var(--ink); }
  .call-text__phone { font-size: 17px; color: #fff; margin-top: 2px; }

  /* back */
  .complete-script { left: 46px; top: 18px; font-size: 70px; color: var(--green); z-index: 2; }
  .headline--car { left: 42px; top: 72px; font-size: 90px; letter-spacing: 1px; }
  .headline--care { left: 42px; top: 140px; font-size: 114px; color: var(--green); letter-spacing: 0; }
  .scope-band { left: 0; top: 257px; width: 400px; height: 33px; background: var(--blue); clip-path: polygon(0 0, 100% 0, 98% 100%, 0 100%); padding: 6px 0 0 38px; font-family: "Russo One", sans-serif; font-style: italic; font-size: 15.5px; color: var(--ink); white-space: nowrap; }
  .intro { left: 38px; top: 306px; width: 372px; font-size: 10.6px; line-height: 13.5px; color: #222; }
  .benefit { font-size: 11px; line-height: 13px; display: flex; gap: 8px; color: #222; }
  .benefit svg { flex: none; margin-top: 1px; }
  .mail-address { left: 419px; top: 46px; font-size: 10px; line-height: 14.6px; color: #222; display: flex; gap: 7px; }
  .mail-divider { left: 557px; top: 48px; width: 1px; height: 52px; background: #222; }
  .postage { left: 570px; top: 46px; font-size: 10px; line-height: 14.6px; color: #111; }
  .route-band { left: 395px; top: 114px; width: 285px; height: 38px; background: var(--blue); clip-path: polygon(0 0, 100% 0, 100% 100%, 9px 100%); padding: 4px 0 0 24px; font-size: 11.4px; line-height: 13px; color: #1a1a1a; }
  .contact-band { left: 0; top: 443px; width: 380px; height: 37px; background: var(--green); clip-path: polygon(0 0, 100% 0, 94% 100%, 0 100%); padding: 0 0 0 38px; display: flex; align-items: center; gap: 14px; font-size: 12px; color: #fff; }
  .contact-band span { display: flex; align-items: center; gap: 8px; }
  .contact-band .sep { width: 1px; height: 14px; background: rgba(255,255,255,.8); }
</style>
</head>
<body>

<section class="postcard postcard--front">
  <svg class="photo-frame" width="680" height="500" aria-hidden="true"><path d="M560 179 H680 V500 H346 L548 186 Q552 179 560 179 Z" fill="var(--blue-light)"/></svg>
  <svg class="photo" width="680" height="500" role="img" aria-label="Photo of a mechanic working under the open hood of a white car in a workshop">
    <defs><linearGradient id="shop1" x1="0" y1="0" x2="0" y2="1"><stop offset="0" stop-color="#d9dcdf"/><stop offset=".55" stop-color="#8f959c"/><stop offset="1" stop-color="#3a3430"/></linearGradient></defs>
    <path d="M572 188 H680 V500 H362 L558 195 Q562 188 572 188 Z" fill="url(#shop1)"/>
  </svg>

  <div class="abs brand"><span class="brand__dot"></span>Copper Kettle Repair</div>
  <div class="abs pickup-banner">Free pickup, drop-off<br>&amp; loaners in Solanco</div>

  <div class="abs script tagline-script">High-quality</div>
  <div class="abs headline headline--auto">AUTO</div>
  <div class="abs headline headline--repair">REPAIR</div>
  <div class="abs script amp">&amp;</div>
  <div class="abs subhead">preventative<br>maintenance!</div>

  <div class="abs info-band">
    <p><svg width="10" height="12" viewBox="0 0 10 12"><path d="M5 0a4.5 4.5 0 0 0-4.5 4.5C.5 8 5 12 5 12s4.5-4 4.5-7.5A4.5 4.5 0 0 0 5 0Zm0 6.3a1.8 1.8 0 1 1 0-3.6 1.8 1.8 0 0 1 0 3.6Z" fill="#111"/></svg>418 Orchard Lane, Unit B, Peach Bottom</p>
    <p><svg width="10" height="12" viewBox="0 0 10 12"><path d="M1 0v11l3-3 2 4 2-1-2-4h4Z" fill="#111"/></svg>CopperKettleRepair.com</p>
  </div>
  <div class="abs call-box"></div>
  <div class="abs call-text">
    <div class="call-text__label">CALL US</div>
    <div class="call-text__phone">717-555-0148</div>
  </div>
</section>

<section class="postcard postcard--back">
  <svg class="photo-frame" width="680" height="500" aria-hidden="true"><path d="M560 180 H680 V500 H346 L548 187 Q552 180 560 180 Z" fill="var(--blue-light)"/></svg>
  <svg class="photo" width="680" height="500" role="img" aria-label="Photo of a technician with a clipboard inspecting a car tyre on a lift">
    <defs><linearGradient id="shop2" x1="0" y1="0" x2="1" y2="1"><stop offset="0" stop-color="#c9b8a2"/><stop offset=".45" stop-color="#6d6f73"/><stop offset="1" stop-color="#2e2c2b"/></linearGradient></defs>
    <path d="M572 189 H680 V500 H362 L558 196 Q562 189 572 189 Z" fill="url(#shop2)"/>
  </svg>

  <div class="abs script complete-script">Complete</div>
  <div class="abs headline headline--car">CAR</div>
  <div class="abs headline headline--care">CARE</div>

  <div class="abs mail-address">
    <svg width="8" height="10" viewBox="0 0 10 12"><path d="M5 0a4.5 4.5 0 0 0-4.5 4.5C.5 8 5 12 5 12s4.5-4 4.5-7.5A4.5 4.5 0 0 0 5 0Zm0 6.3a1.8 1.8 0 1 1 0-3.6 1.8 1.8 0 0 1 0 3.6Z" fill="var(--green)"/></svg>
    <div>Copper Kettle Repair 418<br>Orchard Lane, Unit B<br>Peach Bottom, PA 17563</div>
  </div>
  <div class="abs mail-divider"></div>
  <div class="abs postage">PRSRT STD<br>ECRWSS<br>U.S.POSTAGE<br>PAID EDDM RETAIL</div>
  <div class="abs route-band">****************ECRWSS****EDDM Local<br>Postal Customer.</div>

  <div class="abs scope-band">INCLUDING INSPECTIONS AND EMISSIONS</div>

  <p class="abs intro">Don't trust your car to just any automotive repair shop. We have the reliable, experienced technicians to quickly diagnose what's wrong andfix it right the first time—saving you time, headaches and money.</p>

  <div class="abs benefit" style="left:38px;top:366px">
    <svg width="11" height="9" viewBox="0 0 11 9"><rect x="0" y="2" width="11" height="7" fill="var(--green)"/><rect x="3" y="0" width="5" height="3" fill="var(--green)"/></svg>
    <span>Trust in a timely,<br>full-service repair facility.</span>
  </div>
  <div class="abs benefit" style="left:234px;top:366px">
    <svg width="10" height="9" viewBox="0 0 10 9"><rect x="0" y="4" width="2.5" height="5" fill="var(--green)"/><path d="M3.5 4 6 0c1 0 1.2.8 1 1.6L6.6 3.5H9.5c.5 0 .7.5.5 1L8.7 9H3.5Z" fill="var(--green)"/></svg>
    <span>Enjoy unparalleled<br>customer service</span>
  </div>
  <div class="abs benefit" style="left:38px;top:401px">
    <svg width="10" height="10" viewBox="0 0 10 10"><circle cx="5" cy="2" r="2" fill="var(--green)"/><rect x="1" y="5" width="8" height="5" rx="1" fill="var(--green)"/></svg>
    <span>Enjoy unparalleled<br>customer service</span>
  </div>

  <div class="abs contact-band">
    <span><svg width="12" height="12" viewBox="0 0 12 12"><path d="M2.4 0 4.5 2.6 3.3 4.1a7 7 0 0 0 4.6 4.6l1.5-1.2L12 9.6 10.6 12C5 11.6.4 7 0 1.4Z" fill="#fff"/></svg>717-555-0148</span>
    <span class="sep"></span>
    <span><svg width="10" height="12" viewBox="0 0 10 12"><path d="M1 0v11l3-3 2 4 2-1-2-4h4Z" fill="#fff"/></svg>CopperKettleRepair.com</span>
  </div>
</section>

</body>
</html>
```